Silverleaf Rise Accounting Program

size of ad Full: 7” x 9.6”
1- this is for a ladies program so it should appeal to women.
2-however, I do not want any pictures of people in this ad.
3-all the text should be seen and not covered over by graphics.
4-It should be an ad that will draw people's attention and people should look at it and say it looks nice I want to see that ad.
5-I have put all the instructions in yellow in the file below.
6-please leave 1 inch for the footer .
good luck with this project

• no picture or vector of people.

```html
<!DOCTYPE html>
<html lang="en">
<head>
<meta charset="utf-8">
<title>Silverleaf Rise Accounting Program – Master's in Accounting</title>
<link href="https://fonts.googleapis.com/css2?family=Open+Sans:ital,wght@0,400;0,600;0,700;0,800;1,400&family=Oswald:wght@600&display=swap" rel="stylesheet">
<style>
  :root {
    --ink: #231f20;
    --amber: #e08a0b;
    --gold: #eab30c;
    --leaf: #f5d9b0;
    --rule: #8c8680;
    --paper: #ffffff;
  }
  html, body {
    margin: 0;
    width: 1200px;
    height: 1200px;
    overflow: hidden;
    background: var(--paper);
    font-family: "Open Sans", Arial, sans-serif;
    color: var(--ink);
  }
  .ad { position: relative; width: 1200px; height: 1200px; }
  .backdrop { position: absolute; inset: 0; }
  .text { position: absolute; margin: 0; white-space: nowrap; line-height: 1; }
  .rule { position: absolute; height: 0; border-top: 1px solid var(--rule); }

  .burst-label {
    font-family: "Oswald", "Arial Narrow", sans-serif;
    font-weight: 600;
    font-variant: small-caps;
    font-size: 19px;
    letter-spacing: 1.5px;
    fill: var(--ink);
  }

  .attention {
    position: absolute;
    left: 532px; top: 189px;
    width: 293px; height: 46px;
    background: var(--ink);
    color: var(--paper);
    font-size: 28px;
    letter-spacing: 0.5px;
    display: flex; align-items: center; justify-content: center;
  }
  .headline { left: 374px; top: 242px; font-size: 45px; letter-spacing: -1.5px; }
  .headline .accent { color: var(--amber); }
  .subject { left: 360px; top: 288px; font-size: 58px; font-weight: 700; letter-spacing: 9px; }
  .promise { left: 364px; top: 354px; font-size: 19.5px; line-height: 24.5px; white-space: normal; width: 480px; }

  .advantage { left: 304px; width: 600px; text-align: center; font-size: 24px; font-weight: 700; }
  .advantage .accent { color: var(--amber); }

  .stat-box {
    position: absolute;
    left: 360px; top: 542px;
    width: 134px; height: 79px;
    background: var(--amber);
    border: 1px solid #9a5e08;
    color: var(--paper);
    font-size: 50px; font-weight: 800;
    display: flex; align-items: center; justify-content: center;
  }
  .stat-label { left: 517px; top: 578px; font-size: 30px; font-weight: 600; letter-spacing: 3.2px; color: var(--amber); }
  .fact { left: 358px; font-size: 23.2px; }
  .note { left: 356px; top: 703px; font-size: 15.5px; }

  .badge { position: absolute; left: 362px; top: 762px; width: 100px; height: 142px; }

  .event { right: 346px; text-align: right; }
  .event-title { top: 821px; font-size: 19px; font-weight: 700; letter-spacing: 1.4px; }
  .event-date { top: 845px; font-size: 18.5px; font-weight: 700; color: var(--amber); }
  .event-info { top: 867px; font-size: 16.5px; font-style: italic; }
  .event-contact { top: 888px; font-size: 18.5px; font-weight: 700; color: var(--amber); letter-spacing: 0.3px; }

  .accreditation { left: 304px; width: 604px; top: 946px; text-align: center; font-size: 16.5px; line-height: 21px; white-space: normal; }
</style>
</head>
<body>
<main class="ad">
  <svg class="backdrop" width="1200" height="1200" viewBox="0 0 1200 1200" aria-hidden="true">
    <rect class="frame" x="237" y="100" width="734" height="1008" fill="var(--paper)" stroke="#8a8a8a" stroke-width="1"/>
    <path class="leaf" d="M604 101 C720 200 870 380 905 560 C915 620 913 690 905 740 C880 900 760 1000 604 1106 C448 1000 328 900 303 740 C295 690 293 620 303 560 C338 380 488 200 604 101 Z" fill="var(--leaf)" stroke="#d9b88a" stroke-width="1"/>
    <polygon class="burst" fill="var(--gold)" stroke="#6b6150" stroke-width="1"
      points="426,178 391,187 419,206 382,202 399,229 366,215 369,245 345,221 334,250 323,221 299,245 302,215 269,229 286,202 249,206 277,187 242,178 277,169 249,150 286,154 269,127 302,141 299,111 323,135 334,106 345,135 369,111 366,141 399,127 382,154 419,150 391,169"/>
    <text class="burst-label" x="334" y="172" text-anchor="middle">Masters in</text>
    <text class="burst-label" x="334" y="194" text-anchor="middle">12 Months</text>
  </svg>

  <div class="attention">ATTENTION WOMEN</div>
  <p class="text headline">A <span class="accent">MASTER’S DEGREE</span> IN</p>
  <p class="text subject">ACCOUNTING</p>
  <div class="rule" style="left:362px; top:350px; width:475px;"></div>
  <p class="text promise">A stable, lucrative career, with high-paying, full / part time opportunities in Private/Public companies</p>
  <div class="rule" style="left:362px; top:408px; width:475px;"></div>

  <p class="text advantage" style="top:446px;">THE <span class="accent">HALDEN JOB</span></p>
  <p class="text advantage" style="top:481px;">PLACEMENT ADVANTAGE</p>

  <div class="stat-box">96%</div>
  <p class="text stat-label">PLACEMENT RATE</p>
  <div class="rule" style="left:360px; top:621px; width:474px;"></div>
  <p class="text fact" style="top:628px;">6 placement directors</p>
  <p class="text fact" style="top:658px;">Decades of relationships with 100’s of firms</p>
  <div class="rule" style="left:355px; top:691px; width:481px;"></div>
  <p class="text note">Graduates have been placed in top companies (full/part time jobs).</p>

  <svg class="badge" viewBox="0 0 100 142" role="img" aria-label="Ranking badge">
    <defs>
      <radialGradient id="badgeTone" cx="0.45" cy="0.4" r="0.6">
        <stop offset="0" stop-color="#f3c53a"/>
        <stop offset="1" stop-color="#e07f12"/>
      </radialGradient>
    </defs>
    <circle cx="50" cy="58" r="42" fill="url(#badgeTone)"/>
  </svg>

  <p class="text event event-title">MEETWELL OPEN HOUSE,</p>
  <p class="text event event-date">Sunday June 14, 2 pm</p>
  <p class="text event event-info">for a meetwell&nbsp; link / conference number /information</p>
  <p class="text event event-contact">info@halden.org or 555 014 2200x 111</p>

  <div class="rule" style="left:359px; top:932px; width:502px;"></div>
  <p class="text accreditation">Marlowe Crest University, Masters in Accounting program,<br>received the highest possible rating in USA</p>
</main>
</body>
</html>
```